Pool & Hot Tub Company Need Vehicle Wrap Designs

We need vehicle wrap designs for a Pool & Hot Tub company based in Vancouver, Canada. We do weekly maintenance and repairs. These wraps will be for a 2022 Halvorden Kesta. We are looking for something clean and modern but not boring with a bunch of lines and text. Although we service both pools and hot tubs, this design needs to be hot tub specific. We will be needing future designs for the pool division as well as the repair division, and we would like them all to be cohesive but each have their own differences highlighting their specific divisions. This design will be specifically for the hot tub division. Colours to be used are, White, Blue, Black, Grey. The specific vehicle used is a 2022 Halvorden Kesta, please use that in the mockup. If not able to use a Kesta, please use a small SUV, but Kesta is definitely preferred.
Creative freedom is encouraged. Please include the following info as a minimum: Website, Phone, Email, Services Provided.

www.ferncrestpoolandspa.com
(604)555-0183
service@ferncrestpools.com

Services Provided:
*Weekly Maintenace.
*Repairs.
*Water Changes.

Target Market(s)

Mid to Upper Class Clientel with $200k+/year salary

Industry/Entity Type

Pool & Hot Tub Service - Weekly Water Maintenance & Repairs

Font styles to use
Sans Serif

Colors
0054AA
0677BA
7BADD7
CADEEF
E8F1F8
0094D4
00A9DD
6FCCEA
C7EBF8
E9F6FB
00AB8E
00BBA5
67D7C9
C6EFE9
E9F9F6

Requirements
Must have
• Our logo , services provided, contact info, website.
Should not have
• A bunch of text an clustered design

```html
<!DOCTYPE html>
<html lang="en">
<head>
<meta charset="utf-8">
<title>Ferncrest Pool &amp; Spa — Hot Tub Division Vehicle Wrap</title>
<link rel="stylesheet" href="https://fonts.googleapis.com/css2?family=Montserrat:wght@600&family=Roboto:ital,wght@0,400;0,700;1,700&display=swap">
<style>
  :root {
    --backdrop: #379bfd;
    --navy: #06224f;
    --sky: #6fcfef;
    --sky-soft: #c7ebf8;
    --white: #ffffff;
    --blue-mid: #1b8fd6;
    --blue-deep: #0a6fb0;
    --accent: #0094d4;
    --ink: #0b2a55;
  }
  * { margin: 0; padding: 0; box-sizing: border-box; }
  html, body {
    width: 1200px; height: 900px; overflow: hidden;
    background: var(--backdrop);
  }
  .canvas {
    position: relative; width: 1200px; height: 900px;
    display: flex; align-items: center; justify-content: center;
  }
  .wrap-panel {
    width: 1100px; height: 440px;
    border-radius: 28px; overflow: hidden;
    box-shadow: 0 18px 40px rgba(0, 30, 80, 0.25);
  }
  .wrap-panel svg { display: block; }
  .brand-name {
    font-family: "Montserrat", sans-serif; font-weight: 600;
    fill: var(--ink); letter-spacing: 3px;
  }
  .contact-line {
    font-family: "Roboto", sans-serif; font-weight: 400;
    fill: var(--ink); font-size: 18px;
  }
  .phone {
    font-family: "Roboto", sans-serif; font-weight: 700;
    fill: var(--white); font-size: 44px;
  }
  .services {
    font-family: "Roboto", sans-serif; font-weight: 700; font-style: italic;
    fill: var(--navy); font-size: 19px;
  }
</style>
</head>
<body>
<main class="canvas">
  <section class="wrap-panel" aria-label="Ferncrest Pool &amp; Spa side wrap">
    <svg width="1100" height="440" viewBox="0 0 1100 440" xmlns="http://www.w3.org/2000/svg">
      <defs>
        <linearGradient id="bodyFade" x1="0" y1="0" x2="1" y2="0">
          <stop offset="0" stop-color="var(--sky)"/>
          <stop offset="0.3" stop-color="var(--sky-soft)"/>
          <stop offset="0.55" stop-color="var(--white)"/>
          <stop offset="1" stop-color="var(--white)"/>
        </linearGradient>
        <linearGradient id="lowerBlue" x1="0" y1="0" x2="0" y2="1">
          <stop offset="0" stop-color="var(--blue-mid)"/>
          <stop offset="1" stop-color="var(--blue-deep)"/>
        </linearGradient>
      </defs>

      <rect class="body-fade" width="1100" height="440" fill="url(#bodyFade)"/>

      <g class="brand">
        <circle cx="120" cy="205" r="34" fill="var(--accent)"/>
        <text class="brand-name" x="172" y="200" font-size="30">FERNCREST</text>
        <text class="brand-name" x="174" y="228" font-size="15">POOL &amp; SPA</text>
      </g>

      <g class="diagonal" transform="translate(240 420) rotate(-20)">
        <rect class="field-blue" x="-300" y="70" width="1600" height="600" fill="url(#lowerBlue)"/>
        <rect class="band-navy" x="-300" y="0" width="1600" height="70" fill="var(--navy)"/>

        <text class="contact-line" x="60" y="-12">www.ferncrestpoolandspa.com</text>
        <text class="contact-line" x="330" y="-12">service@ferncrestpools.com</text>
        <text class="phone" x="125" y="52">(604)555-0183</text>

        <text class="services" x="400" y="98">Services Provided:</text>
        <text class="services" x="400" y="124">Weekly Maintenace.</text>
        <text class="services" x="600" y="124">Repairs.</text>
        <text class="services" x="700" y="124">Water Changes.</text>
      </g>
    </svg>
  </section>
</main>
</body>
</html>
```